Zielgruppe
Ich bin Autorin und Verlegerin. Es geht um das Cover für ein neues Buch zum Thema 'Online-PR'. Zielgruppe des Buches sind Anwender des Online-Marketings, wie z.B. Selbständige, kleine und mittlere Unternehmen.
Aufgabenstellung
Das Buch wird der 1. Band einer Buchreihe mit dem Titel 'Kompass Netzwerbung für Einsteiger'. Das Cover sollte daher einen Wiedererkennungswert haben - es sollte für kommende Bücher der Reihe in gewissen Dingen (z.B. Cover-Foto) leicht abwandelbar sein. Name der Autorin, Haupttitel des Buches sowie Titel der Buchreihe müssen auch im Internet bei der üblichen Verkleinerung in Thumbnail-Größe (wi bei Bücherfalke) gut lesbar sein. Benötigt wird die U1 (in 3 oder 4 verschiedenen Formaten) sowie die U4 (Buchrückseite)

```html
<!DOCTYPE html>
<html lang="de">
<head>
<meta charset="utf-8">
<title>Überzeugende Web-Präsenz – Buchcover</title>
<link rel="stylesheet" href="https://fonts.googleapis.com/css2?family=Overpass:wght@400;600;700;800&family=Barlow:wght@600&display=swap">
<style>
  :root {
    --canvas-bg: #eeeeee;
    --cover-bg: #ffffff;
    --title-grey: #464646;
    --subtitle-teal: #2a7895;
    --accent-purple: #7b2d8e;
    --band-teal: #2a7f96;
    --band-text: #ffffff;
    --photo-warm: #b98d72;
    --photo-cool: #c9ccd6;
    --photo-green: #6f8a5a;
  }
  * { margin: 0; padding: 0; box-sizing: border-box; }
  html, body {
    width: 900px;
    height: 1200px;
    overflow: hidden;
    background: var(--canvas-bg);
  }
  .book-cover {
    position: absolute;
    left: 70px;
    top: 30px;
    width: 760px;
    height: 1140px;
    background: var(--cover-bg);
    box-shadow: 0 2px 6px rgba(0,0,0,0.18);
    font-family: "Overpass", sans-serif;
  }
  .cover-title {
    position: absolute;
    left: 48px;
    top: 178px;
    font-weight: 800;
    font-size: 94px;
    line-height: 104px;
    color: var(--title-grey);
    letter-spacing: 0.5px;
    white-space: nowrap;
  }
  .cover-subtitle {
    position: absolute;
    left: 48px;
    top: 412px;
    font-weight: 600;
    font-size: 29px;
    line-height: 38px;
    color: var(--subtitle-teal);
    white-space: nowrap;
  }
  .cover-rule {
    position: absolute;
    left: 46px;
    top: 563px;
    width: 590px;
    height: 3px;
    background: var(--accent-purple);
  }
  .cover-photo {
    position: absolute;
    left: 46px;
    top: 587px;
    width: 590px;
    height: 350px;
    background:
      linear-gradient(90deg, var(--photo-warm) 0%, #d7b9a3 35%, var(--photo-green) 60%, var(--photo-cool) 100%);
  }
  .author-band {
    position: absolute;
    left: 254px;
    top: 898px;
    width: 462px;
    height: 92px;
    background: var(--accent-purple);
    color: var(--band-text);
    font-weight: 600;
    font-size: 42px;
    line-height: 98px;
    text-align: center;
    white-space: nowrap;
  }
  .series-band {
    position: absolute;
    left: 254px;
    top: 1004px;
    width: 462px;
    height: 68px;
    background: var(--band-teal);
    color: var(--band-text);
    font-family: "Barlow", sans-serif;
    font-weight: 600;
    font-size: 23px;
    line-height: 68px;
    text-align: center;
    white-space: nowrap;
  }
  .publisher-mark {
    position: absolute;
    left: 50px;
    top: 1010px;
    display: flex;
    align-items: center;
    gap: 8px;
    color: var(--accent-purple);
    font-weight: 700;
    font-size: 22px;
  }
  .publisher-mark .mark-dot {
    width: 14px;
    height: 14px;
    border-radius: 50%;
    background: var(--accent-purple);
  }
</style>
</head>
<body>
  <main class="book-cover">
    <h1 class="cover-title">Überzeugende<br>Web-Präsenz.</h1>
    <p class="cover-subtitle">Mehr Aufmerksamkeit und größere Resonanz<br>für Ihre Leistungen im Netz</p>
    <div class="cover-rule"></div>
    <div class="cover-photo" role="img" aria-label="Foto: zwei Geschäftsleute geben sich im Büro ein High Five"></div>
    <div class="author-band">Carla Maria Wendt</div>
    <div class="series-band">Kompass Netzwerbung für Einsteiger</div>
    <div class="publisher-mark"><span class="mark-dot"></span><span>Kursfeder</span></div>
  </main>
</body>
</html>
```